School Caterer needs a updated letter head/ business card design

Hi
I operate a school catering business.
I operate school canteens across Melbourne and New South Wales.
My Business is called Brel Corporation Pty Ltd but i trade as Brel Tasa Foods.
Brel is after my patron saint ..St Brel .

I am looking for an update to my Letterhead/Business Card.
Maybe the new design to be a little bit more modern.
Please see upload of current Letterhead business card design.
Need to change the PO address (Po Box 718 Glenmara Vic 3961 )along with adding a website address (Breltasafoods@kestrelmail.com.au) .

Target Market(s)

Schools across Australia

Industry/Entity Type

Business

Contact Information for Business Card

Brel Corporation Pty Ltd
Tam Verotti
Director
0487 312 649
Brelfoods@kestrelmail.com.au
www.breltasafoods.com.au
Po Box 718 Glenmara Vic 3961

Font styles to use
Decorative

Colors

Designer to choose colors to be used in the design.

Requirements
Must have
• A modern design, but with keeping with a homely feel.
• New PO Address ( PO Box 718 Glenmara Vic 3961)
• New website (www.breltasafoods.com.au)
Nice to have
• The current logo, but happy to see modern designs.

```html
<!DOCTYPE html>
<html lang="en">
<head>
<meta charset="utf-8">
<title>Brel Tasa Foods – Letterhead &amp; Business Cards</title>
<link rel="stylesheet" href="https://fonts.googleapis.com/css2?family=Ubuntu:wght@400;500&family=Lato:wght@300;400&display=swap">
<style>
  :root {
    --brand-blue: #1589d6;
    --ink: #1c1c1c;
    --paper: #fbfbfb;
    --backdrop: #dcdcdc;
    --line-art: #eceeef;
  }
  * { margin: 0; padding: 0; box-sizing: border-box; }
  html, body { width: 1200px; height: 900px; overflow: hidden; background: var(--backdrop); }
  .canvas { position: relative; width: 1200px; height: 900px; }

  .wordmark {
    font-family: "Lato", sans-serif;
    font-weight: 400;
    color: var(--brand-blue);
    text-align: center;
    white-space: nowrap;
    line-height: 1;
  }

  /* Letterhead */
  .letterhead {
    position: absolute; left: 277px; top: 98px; width: 490px; height: 691px;
    background: var(--paper);
    box-shadow: 0 2px 6px rgba(0,0,0,.18);
  }
  .letterhead .wordmark { position: absolute; left: 0; right: 0; top: 72px; font-size: 28px; }
  .letter-art {
    position: absolute; left: 243px; top: 382px; width: 244px; height: 306px;
    background: radial-gradient(ellipse at 60% 55%, var(--line-art) 0%, rgba(236,238,239,0) 70%);
  }
  .letter-topic {
    position: absolute; left: 44px; top: 157px;
    font-family: "Ubuntu", sans-serif; font-weight: 500; font-size: 9.5px; color: var(--ink);
  }
  .letter-body {
    position: absolute; left: 44px; top: 193px; width: 412px;
    font-family: "Lato", sans-serif; font-weight: 300; font-size: 8.6px; line-height: 10.8px;
    color: var(--ink); text-align: justify; letter-spacing: -0.15px;
  }
  .letter-body p { margin-bottom: 10.8px; }
  .letter-signoff { position: absolute; left: 44px; top: 532px; font-family: "Ubuntu", sans-serif; color: var(--ink); }
  .signoff-name { font-size: 9px; }
  .signoff-role { font-size: 6px; letter-spacing: .3px; margin-top: 3px; }
  .signature {
    position: absolute; left: 42px; top: 558px; width: 56px; height: 26px;
    background: linear-gradient(90deg, rgba(30,40,80,.12), rgba(30,40,80,.05));
    border-radius: 3px;
  }
  .letter-footer {
    position: absolute; left: 0; right: 0; top: 645px;
    font-family: "Ubuntu", sans-serif; font-size: 7.8px; line-height: 13px; color: var(--ink); text-align: center;
  }
  .letter-footer .sep { color: var(--brand-blue); margin: 0 4px; }

  /* Cards */
  .card {
    position: absolute; width: 128px; height: 200px;
    box-shadow: 2px 3px 6px rgba(0,0,0,.22);
    overflow: hidden;
  }
  .card-back { left: 879px; top: 106px; background: var(--brand-blue); color: #fff; }
  .card-front { left: 878px; top: 366px; background: var(--paper); }
  .card .wordmark { position: absolute; left: 0; right: 0; top: 46px; font-size: 15px; }
  .card-back .wordmark { color: #fff; }
  .card-back-texture {
    position: absolute; inset: 0;
    background: radial-gradient(ellipse at 50% 45%, rgba(255,255,255,.07), rgba(255,255,255,0) 70%);
  }
  .sprout-icon {
    position: absolute; left: 52px; top: 137px; width: 24px; height: 11px;
    background: rgba(255,255,255,.55); border-radius: 12px 12px 3px 3px;
  }
  .tagline {
    position: absolute; left: 0; right: 0; top: 153px;
    font-family: "Ubuntu", sans-serif; font-size: 8.2px; line-height: 10.5px; text-align: center;
  }
  .card-front-art {
    position: absolute; left: 0; top: 90px; width: 128px; height: 110px;
    background: radial-gradient(ellipse at 40% 60%, var(--line-art), rgba(236,238,239,0) 75%);
  }
  .contact-name {
    position: absolute; left: 0; right: 0; top: 110px;
    font-family: "Ubuntu", sans-serif; font-weight: 500; font-size: 9.6px; color: var(--brand-blue); text-align: center;
  }
  .contact-details {
    position: absolute; left: 0; right: 0; top: 134px;
    font-family: "Ubuntu", sans-serif; font-size: 6px; line-height: 8px; color: var(--ink); text-align: center;
  }
  .contact-rule { width: 6px; height: 1.2px; background: var(--brand-blue); margin: 5px auto 7px; }
</style>
</head>
<body>
<div class="canvas">

  <section class="letterhead">
    <div class="wordmark">Brel Tasa Foods</div>
    <div class="letter-art" role="img" aria-label="Faint line illustration of a chopping board, knife and vegetables"></div>

    <h1 class="letter-topic">Today’s topic</h1>
    <div class="letter-body">
      <p>Lorem ipsum dolor sit amet, consectetur adipisicing elit, sed do eiusmod tempor incididunt ut labore et dolore magna aliqua. Ut enim ad minim veniam, quis nostrud exercitation ullamco laboris nisi ut aliquip ex ea commodo consequat.</p>
      <p>Duis aute irure dolor in reprehenderit in voluptate velit esse cillum dolore eu fugiat nulla pariatur. Excepteur sint occaecat cupidatat non proident, sunt in culpa qui officia deserunt mollit anim id est laborum.</p>
      <p>Sed ut perspiciatis unde omnis iste natus error sit voluptatem accusantium doloremque laudantium, totam rem aperiam, eaque ipsa quae ab illo inventore veritatis et quasi architecto beatae vitae dicta sunt explicabo.</p>
      <p>Nemo enim ipsam voluptatem quia voluptas sit aspernatur aut odit aut fugit, sed quia consequuntur magni dolores eos qui ratione voluptatem sequi nesciunt. Neque porro quisquam est, qui dolorem ipsum quia dolor sit amet, consectetur, adipisci velit, sed quia non numquam eius modi tempora incidunt ut labore et dolore magnam aliquam quaerat voluptatem.</p>
      <p>Ut enim ad minima veniam, quis nostrum exercitationem ullam corporis suscipit laboriosam, nisi ut aliquid ex ea commodi consequatur?</p>
      <p>Quis autem vel eum iure reprehenderit qui in ea voluptate velit esse quam nihil molestiae consequatur, vel illum qui dolorem eum fugiat quo voluptas nulla pariatur?</p>
      <p>Duis aute irure dolor in reprehenderit in voluptate velit esse cillum dolore eu fugiat nulla pariatur. Excepteur sint occaecat cupidatat non proident, sunt in culpa qui officia deserunt mollit anim id est laborum.</p>
      <p>Lorem ipsum dolor sit amet, consectetur adipisicing elit, sed do eiusmod tempor incididunt ut labore et dolore magna aliqua. Ut enim ad minim veniam, quis nostrud exercitation ullamco laboris nisi ut aliquip ex ea commodo consequat.</p>
    </div>

    <div class="letter-signoff">
      <div class="signoff-name">Brel Tasa</div>
      <div class="signoff-role">OWNER</div>
    </div>
    <div class="signature" role="img" aria-label="Handwritten signature"></div>

    <footer class="letter-footer">
      0487 312 649<span class="sep">|</span>Breltasafoods@kestrelmail.com.au<span class="sep">|</span>www.breltasafoods.com.au<br>
      Po Box 718 Glenmara Vic 3961
    </footer>
  </section>

  <section class="card card-back">
    <div class="card-back-texture" role="img" aria-label="Subtle tonal pattern of kitchen line drawings"></div>
    <div class="wordmark">Brel Tasa Foods</div>
    <div class="sprout-icon" role="img" aria-label="Small sprout emblem"></div>
    <div class="tagline">Healthy &amp; Nutritious<br>School Catering</div>
  </section>

  <section class="card card-front">
    <div class="card-front-art" role="img" aria-label="Faint line illustration of cooking utensils and food"></div>
    <div class="wordmark">Brel Tasa Foods</div>
    <div class="contact-name">Brel Tasa</div>
    <div class="contact-details">
      0487 312 649<br>
      Breltasafoods@kestrelmail.com.au<br>
      www.breltasafoods.com.au
      <div class="contact-rule"></div>
      Po Box 718<br>
      Glenmara Vic 3961
    </div>
  </section>

</div>
</body>
</html>
```